Tallgrove Vale Management

I need a professional website. My current website is tallgrovevalemanagement.com and I hate it. It was created with some AI tool very quickly because I needed a site up and running with no advanced notice. I’m open to all designs .. I trust you, the professionals will deliver the results I’m anxiously awaiting! :)

```html
<!DOCTYPE html>
<html lang="en">
<head>
<meta charset="utf-8">
<title>Tallgrove Vale Management</title>
<link href="https://fonts.googleapis.com/css2?family=Poppins:ital,wght@0,400;0,500;0,600;0,700;1,400&display=swap" rel="stylesheet">
<style>
:root{
  --navy:#1f3160;
  --navy-deep:#16244a;
  --navy-card:#1a2850;
  --red:#8b1a2b;
  --ink:#222;
  --muted:#555;
  --line:#d6d6d6;
  --white:#fff;
}
*{margin:0;padding:0;box-sizing:border-box}
html,body{width:1200px;height:4862px;overflow:hidden}
body{font-family:'Poppins',sans-serif;color:var(--ink);background:var(--white);position:relative}
.abs{position:absolute}
a{color:inherit;text-decoration:none}

/* top bar */
.topbar{left:0;top:0;width:1200px;height:38px;background:var(--navy);color:#fff;font-size:12px}
.topbar .dot{position:absolute;top:12px;width:14px;height:14px;border:1.5px solid #fff;border-radius:50%}
.topbar .contact{position:absolute;top:10px;display:flex;align-items:center;gap:8px}

/* nav */
.nav{left:0;top:38px;width:1200px;height:85px;background:#fff}
.brand{position:absolute;left:160px;top:52px;width:120px;font-size:12px;font-weight:700;color:var(--navy);line-height:15px}
.menu{position:absolute;top:72px;font-size:13px;color:#333}
.menu.active{color:var(--red);font-weight:500}
.btn{display:flex;align-items:center;justify-content:center;background:var(--red);color:#fff;font-size:12px}
.book{left:877px;top:60px;width:161px;height:40px;font-weight:600}

/* hero */
.hero{left:0;top:123px;width:1200px;height:688px;background:linear-gradient(100deg,#2c3441 0%,#3b4250 35%,#6b6358 60%,#9a8b76 80%,#4a4c55 100%)}
.hero-shade{left:0;top:123px;width:1200px;height:688px;background:linear-gradient(90deg,rgba(20,25,35,.55),rgba(20,25,35,.1))}
.hero h1{left:160px;top:296px;width:560px;font-size:46px;font-weight:600;line-height:54px;color:#fff}
.hero-tag{left:162px;top:464px;font-size:13px;color:#fff}
.hero-btn{left:162px;top:510px;width:136px;height:37px}

/* about */
.eyebrow{font-size:13px;color:#333}
.about-eyebrow{left:160px;top:898px}
.h2{font-size:30px;font-weight:600;color:var(--ink)}
.about-title{left:160px;top:922px}
.about-copy{left:160px;top:975px;width:370px;font-size:13px;line-height:20px;color:#444}
.about-copy p{margin-bottom:19px}
.about-btn{left:162px;top:1291px;width:138px;height:37px}
.photo-main{left:636px;top:902px;width:402px;height:441px;background:linear-gradient(135deg,#cfd3d6,#8a9198 55%,#41505e)}
.photo-small{left:583px;top:1247px;width:215px;height:172px;background:linear-gradient(135deg,#b8bfc6,#6f7780);border:3px solid #fff}

/* how it works */
.how-bg{left:0;top:1553px;width:1200px;height:494px;background:var(--navy)}
.center{text-align:center;width:1200px;left:0}
.how-title{top:1601px;color:#fff}
.how-sub{top:1650px;font-size:13px;color:#fff}
.step{top:1711px;width:218px;height:244px;background:#fff;padding:0 19px}
.step svg.icon{position:absolute;left:19px;top:40px}
.step h3{position:absolute;left:19px;top:104px;font-size:15px;font-weight:600;color:var(--ink)}
.step p{position:absolute;left:19px;top:132px;width:180px;font-size:11px;line-height:14px;color:#555}
.step .more{position:absolute;left:19px;top:193px;display:flex;align-items:center;gap:8px;font-size:10px;font-weight:500;color:#333}

/* services */
.svc-bg{left:0;top:2047px;width:1200px;height:1466px;background:linear-gradient(160deg,#2a3d6d 0%,#1f3160 45%,#243764 70%,#1a2a55 100%)}
.svc-title{top:2175px;color:#fff}
.svc-sub{top:2223px;font-size:13px;color:#fff}
.svc-card{width:415px;height:485px;background:var(--navy-card)}
.svc-card .shot{position:absolute;left:20px;top:20px;width:375px;height:353px}
.svc-card h3{position:absolute;left:22px;top:397px;font-size:19px;font-weight:600;color:#fff}
.svc-card p{position:absolute;left:22px;top:433px;width:370px;font-size:10.5px;line-height:13px;color:#fff}
.svc-btn{left:519px;top:3457px;width:162px;height:38px;font-size:13px}

/* reviews */
.rev-title{top:3566px}
.rev-sub{top:3616px;font-size:13px;color:#333}
.review{top:3670px;width:514px;height:232px;border:1px solid #dcdcdc;border-radius:10px;background:#fff}
.review .avatar{position:absolute;left:20px;top:42px;width:60px;height:60px;border-radius:50%;background:linear-gradient(135deg,#9aa3ad,#4e5864)}
.review .sign{position:absolute;left:98px;top:42px;width:78px;height:36px;background:linear-gradient(90deg,#e7e7e7,#f3f3f3)}
.review .stars{position:absolute;left:210px;top:50px;font-size:19px;letter-spacing:1px;color:#333}
.review .quote{position:absolute;right:30px;top:22px;font-size:90px;line-height:90px;color:#dedede;font-weight:700}
.review .name{position:absolute;left:98px;top:86px;font-size:14px;color:#333}
.review .name b{font-weight:600}
.review p{position:absolute;left:98px;top:118px;width:390px;font-size:12.5px;line-height:22.5px;font-style:italic;color:#666}
.chev{top:3770px}
.dots{top:3942px;left:570px;display:flex;gap:6px;align-items:center}
.dots span{width:7px;height:7px;border-radius:50%;background:#a8b0c8}
.dots span.on{width:20px;border-radius:4px;background:var(--red)}

/* contact */
.form-card{left:345px;top:4027px;width:506px;height:577px;background:#fff;box-shadow:0 0 30px rgba(0,0,0,.06)}
.contact-eyebrow{left:345px;width:506px;text-align:center;top:4071px;font-size:13px}
.contact-title{left:345px;width:506px;text-align:center;top:4092px}
.field{border-bottom:1px solid var(--line);font-size:11px;color:#777;padding-bottom:12px}
.captcha{left:485px;top:4476px;width:228px;height:58px;border:1px solid #d3d3d3;background:#f9f9f9;border-radius:3px;font-size:11px;color:#333}
.captcha .box{position:absolute;left:12px;top:19px;width:20px;height:20px;border:2px solid #c1c1c1;background:#fff;border-radius:2px}
.captcha .label{position:absolute;left:42px;top:21px}
.captcha .mark{position:absolute;right:18px;top:14px;width:20px;height:20px;border-radius:50%;background:#bcc4d4}
.submit{left:522px;top:4557px;width:153px;height:38px;font-size:13px;font-weight:600;border-radius:6px}

/* footer */
.footer{left:0;top:4604px;width:1200px;height:258px;background:var(--navy);color:#fff}
.foot-brand{left:180px;top:4712px;width:150px;font-size:17px;font-weight:700;line-height:22px;color:#fff}
.foot-h{font-size:19px;font-weight:500;color:#fff}
.foot-rule{height:2px;background:#fff}
.foot-link{font-size:12px;color:#fff}
.news-input{left:651px;top:4727px;width:234px;height:34px;background:#fff;font-size:10px;color:#999;padding:10px 8px}
.subscribe{left:894px;top:4727px;width:131px;height:34px;font-size:13px;font-weight:600}
.foot-dot{width:13px;height:13px;border:1.5px solid #fff;border-radius:50%;top:4789px}
.copy{left:762px;top:4787px;font-size:11px;color:#fff}
</style>
</head>
<body>

<!-- top bar -->
<div class="abs topbar">
  <span class="dot" style="left:158px"></span>
  <span class="dot" style="left:196px"></span>
  <span class="dot" style="left:236px"></span>
  <div class="contact" style="left:640px">
    <svg width="12" height="12" viewBox="0 0 24 24"><path fill="#fff" d="M6.6 10.8a15 15 0 0 0 6.6 6.6l2.2-2.2c.3-.3.7-.4 1-.2 1.1.4 2.3.6 3.6.6.6 0 1 .4 1 1V20c0 .6-.4 1-1 1A17 17 0 0 1 3 4c0-.6.4-1 1-1h3.5c.6 0 1 .4 1 1 0 1.3.2 2.5.6 3.6.1.3 0 .7-.2 1z"/></svg>
    <span>+1 555 014 2290</span>
  </div>
  <div class="contact" style="left:785px">
    <svg width="13" height="10" viewBox="0 0 26 20"><rect x="1" y="1" width="24" height="18" fill="#fff"/><path d="M1 1l12 9 12-9" stroke="#1f3160" stroke-width="2" fill="none"/></svg>
    <span>info@tallgrovevalemanagement.com</span>
  </div>
</div>

<!-- navigation -->
<div class="abs nav"></div>
<div class="brand">Tallgrove Vale<br>Management</div>
<a class="abs menu active" style="left:296px">Home</a>
<a class="abs menu" style="left:372px">About Us</a>
<a class="abs menu" style="left:483px">Services</a>
<a class="abs menu" style="left:581px">How It Works</a>
<a class="abs menu" style="left:710px">News</a>
<a class="abs menu" style="left:785px">Contact Us</a>
<a class="abs btn book">BOOK CONSULTATION</a>

<!-- hero -->
<div class="abs hero" role="img" aria-label="Modern two-storey villa with pool at dusk"></div>
<div class="abs hero-shade"></div>
<h1 class="abs" style="left:160px;top:296px;width:560px;font-size:46px;font-weight:600;line-height:54px;color:#fff">Professional Property Management You Can Trust</h1>
<div class="abs hero-tag">A true partner, not just a vendor.</div>
<a class="abs btn hero-btn">Learn More</a>
<svg class="abs" style="left:0;top:700px" width="1200" height="112" viewBox="0 0 1200 112">
  <path d="M0 27 C400 120 800 95 1200 25 L1200 112 L0 112Z" fill="#8b1a2b"/>
  <path d="M0 27 C380 112 760 112 1200 55 L1200 112 L0 112Z" fill="#fff"/>
</svg>

<!-- about -->
<div class="abs eyebrow about-eyebrow">About Us</div>
<h2 class="abs h2 about-title">Who We Are</h2>
<div class="abs about-copy">
  <p>Every pleasure is to be welcomed and every pain avoided. But in certain circumstances and owing to the claims of duty obligations of business it will frequently occur that.</p>
  <p>If you're able to become pregnant, you should use effective and reliable birth control while taking a GLP-1 agonist. If you become pregnant while taking the immediately.</p>
  <p>If you're able to become pregnant, you should use effective and reliable birth control while taking a GLP-1 agonist. If you become pregnant while taking the medication, see your healthcare provider immediately.</p>
</div>
<a class="abs btn about-btn">Learn More</a>
<div class="abs photo-main" role="img" aria-label="Business partners shaking hands over a model of buildings and trees"></div>
<div class="abs photo-small" role="img" aria-label="Two colleagues reviewing documents at a desk"></div>

<!-- how it works -->
<svg class="abs" style="left:0;top:1487px" width="1200" height="67" viewBox="0 0 1200 67"><path d="M180 67 L1200 0 L1200 67Z" fill="#8b1a2b"/></svg>
<div class="abs how-bg"></div>
<h2 class="abs h2 center how-title" style="color:#fff">How It Works</h2>
<div class="abs center how-sub">Together, we help our clients achieve tangible, measurable results.</div>

<div class="abs step" style="left:234px">
  <svg class="icon" width="34" height="34" viewBox="0 0 24 24"><path fill="#1f3160" d="M6.6 10.8a15 15 0 0 0 6.6 6.6l2.2-2.2c.3-.3.7-.4 1-.2 1.1.4 2.3.6 3.6.6.6 0 1 .4 1 1V20c0 .6-.4 1-1 1A17 17 0 0 1 3 4c0-.6.4-1 1-1h3.5c.6 0 1 .4 1 1 0 1.3.2 2.5.6 3.6.1.3 0 .7-.2 1z"/></svg>
  <h3>Consultation</h3>
  <p>We always provide people a complete solution focused of any business.</p>
  <div class="more"><svg width="22" height="10" viewBox="0 0 22 10"><path d="M0 5h20M16 1l4 4-4 4" stroke="#333" fill="none"/></svg></div>
</div>
<div class="abs step" style="left:489px">
  <svg class="icon" width="34" height="38" viewBox="0 0 34 38"><rect x="9" y="2" width="14" height="20" fill="none" stroke="#1f3160" stroke-width="2.5"/><path d="M12 7h8M12 11h8M12 15h8" stroke="#1f3160" stroke-width="2"/><path d="M2 28c6-4 10-2 14 0h10c3 0 3 4 0 4H14M2 34h24l7-6" stroke="#1f3160" stroke-width="2.5" fill="none"/></svg>
  <h3>Property Assessment</h3>
  <p>We always provide people a complete solution focused of any business.</p>
  <div class="more"><svg width="22" height="10" viewBox="0 0 22 10"><path d="M0 5h20M16 1l4 4-4 4" stroke="#333" fill="none"/></svg></div>
</div>
<div class="abs step" style="left:745px">
  <svg class="icon" width="38" height="34" viewBox="0 0 38 34"><path d="M4 32V24M10 32V19M16 32V15M22 32V11" stroke="#1f3160" stroke-width="4"/><path d="M4 20 L26 4" stroke="#1f3160" stroke-width="2.5"/><path d="M20 3h7v7" stroke="#1f3160" stroke-width="2.5" fill="none"/><path d="M30 10v20h6" stroke="#1f3160" stroke-width="2.5" fill="none"/></svg>
  <h3>Reports &amp; Support</h3>
  <p>We always provide people a complete solution focused of any business.</p>
  <div class="more">Learn More <svg width="22" height="10" viewBox="0 0 22 10"><path d="M0 5h20M16 1l4 4-4 4" stroke="#333" fill="none"/></svg></div>
</div>

<!-- services -->
<div class="abs svc-bg" role="img" aria-label="Dim blue cityscape of tall apartment buildings"></div>
<svg class="abs" style="left:0;top:2047px" width="1200" height="105" viewBox="0 0 1200 105"><path d="M0 0 H1200 V20 L0 104Z" fill="#8b1a2b"/></svg>
<h2 class="abs h2 center svc-title" style="color:#fff">Services We Offer</h2>
<div class="abs center svc-sub">There's a low risk of mild low blood sugar hypoglycemia</div>

<div class="abs svc-card" style="left:160px;top:2315px">
  <div class="shot" role="img" aria-label="White residential house with blue roof among bare trees" style="background:linear-gradient(160deg,#c7ccd3,#8e9299 50%,#5e5a50)"></div>
  <h3>Residential Property Management</h3>
  <p>If your prior authorization is denied, the cost of your GLP-1 it is important to understand the denial reason.</p>
</div>
<div class="abs svc-card" style="left:623px;top:2604px">
  <div class="shot" role="img" aria-label="Modern apartment block with dark and brick facade" style="background:linear-gradient(160deg,#e9ecef,#b0784f 45%,#2d3a4a)"></div>
  <h3>Commercial Property Management</h3>
  <p>If your prior authorization is denied, the cost of your GLP-1 it is important to understand the denial reason.</p>
</div>
<div class="abs svc-card" style="left:160px;top:2870px">
  <div class="shot" role="img" aria-label="Agent reviewing documents with a couple on a sofa" style="background:linear-gradient(160deg,#d8d4cc,#b39a82 50%,#7c6b5d)"></div>
  <h3>Tenant Placement</h3>
  <p>If your prior authorization is denied, the cost of your GLP-1 it is important to understand the denial reason.</p>
</div>
<svg class="abs" style="left:0;top:3470px" width="1200" height="44" viewBox="0 0 1200 44"><path d="M0 43 L1200 0 V44 H0Z" fill="#fff"/></svg>
<a class="abs btn svc-btn">View All Services</a>

<!-- reviews -->
<h2 class="abs h2 center rev-title">Customer Review</h2>
<div class="abs center rev-sub">There's a low risk of mild low blood sugar hypoglycemia</div>
<svg class="abs chev" style="left:50px" width="14" height="24" viewBox="0 0 14 24"><path d="M12 2 L2 12 L12 22" stroke="#555" stroke-width="1.5" fill="none"/></svg>
<svg class="abs chev" style="left:1134px" width="14" height="24" viewBox="0 0 14 24"><path d="M2 2 L12 12 L2 22" stroke="#555" stroke-width="1.5" fill="none"/></svg>

<div class="abs review" style="left:77px">
  <div class="avatar" role="img" aria-label="Reviewer portrait"></div>
  <div class="sign" role="img" aria-label="Handwritten signature"></div>
  <div class="stars">★★★★★</div>
  <div class="quote">”</div>
  <div class="name">Miles Corrigan - <b>Broker Partner</b></div>
  <p>Nora is one of a kind. She has been a key partner to our business and has run the extra mile to ensure our clients are looked after. I highly recommend her for any non-conforming lending scenarios.</p>
</div>
<div class="abs review" style="left:607px">
  <div class="avatar" role="img" aria-label="Reviewer portrait"></div>
  <div class="sign" role="img" aria-label="Handwritten signature"></div>
  <div class="stars">★★★★★</div>
  <div class="quote">”</div>
  <div class="name">Miles Corrigan - <b>Broker Partner</b></div>
  <p>Nora is one of a kind. She has been a key partner to our business and has run the extra mile to ensure our clients are looked after. I highly recommend her for any non-conforming lending scenarios.</p>
</div>
<div class="abs dots"><span></span><span></span><span></span><span class="on"></span></div>

<!-- contact -->
<svg class="abs" style="left:0;top:4170px" width="1200" height="435" viewBox="0 0 1200 435">
  <defs>
    <linearGradient id="cityDusk" x1="0" y1="0" x2="0" y2="1">
      <stop offset="0" stop-color="#3b5a9a"/>
      <stop offset="1" stop-color="#1a2a55"/>
    </linearGradient>
  </defs>
  <path d="M0 435 V240 Q600 -200 1200 220 V435Z" fill="#8b1a2b"/>
  <path d="M0 435 V290 Q600 -130 1200 270 V435Z" fill="url(#cityDusk)" role="img" aria-label="Apartment towers against a dusk sky"/>
</svg>
<div class="abs form-card"></div>
<div class="abs eyebrow contact-eyebrow">Contact</div>
<h2 class="abs h2 contact-title">Get In Touch</h2>
<div class="abs field" style="left:404px;top:4166px;width:177px">Name*</div>
<div class="abs field" style="left:621px;top:4166px;width:177px">Last Name</div>
<div class="abs field" style="left:404px;top:4228px;width:177px">Phone</div>
<div class="abs field" style="left:621px;top:4228px;width:177px">Email Address*</div>
<div class="abs field" style="left:404px;top:4290px;width:394px">Subject</div>
<div class="abs field" style="left:404px;top:4352px;width:394px;height:77px">Your Message</div>
<div class="abs captcha">
  <div class="box"></div>
  <div class="label">I'm not a robot</div>
  <div class="mark"></div>
</div>
<a class="abs btn submit">SUBMIT</a>

<!-- footer -->
<div class="abs footer"></div>
<div class="abs foot-brand">Tallgrove Vale<br>Management</div>
<div class="abs foot-h" style="left:408px;top:4670px">Company</div>
<div class="abs foot-rule" style="left:408px;top:4701px;width:112px"></div>
<a class="abs foot-link" style="left:408px;top:4724px">Home</a>
<a class="abs foot-link" style="left:408px;top:4747px">About Us</a>
<a class="abs foot-link" style="left:408px;top:4770px">Services</a>
<a class="abs foot-link" style="left:408px;top:4793px">Contact Us</a>
<a class="abs foot-link" style="left:491px;top:4724px">Projects</a>
<a class="abs foot-link" style="left:491px;top:4747px">Privacy Policy</a>
<div class="abs foot-h" style="left:651px;top:4670px">Join our Newsletter</div>
<div class="abs news-input">Email Address</div>
<a class="abs btn subscribe">SUBSCRIBE</a>
<span class="abs foot-dot" style="left:651px"></span>
<span class="abs foot-dot" style="left:689px"></span>
<span class="abs foot-dot" style="left:727px"></span>
<div class="abs copy">Copyright©2026. All rights reserved</div>

</body>
</html>
```